Out of School Care Business Needs Design for Indoor Pull-Up Banner & Outdoor Footpath Sign

We provide childcare and fun activities for kids aged between 5 years old and 14 years old. Service is based within local schools. Banner will be ...

Industry/Entity Type

Business

```html
<!DOCTYPE html>
<html lang="en">
<head>
<meta charset="utf-8">
<title>Play Haven – Banners</title>
<link rel="stylesheet" href="https://fonts.googleapis.com/css2?family=Architects+Daughter&family=Lilita+One&family=Open+Sans:wght@400;600&display=swap">
<style>
  :root {
    --blue: #009fe3;
    --pink: #e0097c;
    --yellow: #ffed00;
    --grey: #dadbd9;
    --charcoal: #2e2e2e;
    --white: #ffffff;
    --page: #ffffff;
  }
  * { margin: 0; padding: 0; box-sizing: border-box; }
  html, body {
    width: 1200px; height: 888px; overflow: hidden;
    background: var(--page);
  }
  .banner-set { position: relative; width: 1200px; height: 888px; }
  .banner {
    position: absolute; top: 0; width: 378px; height: 888px;
    overflow: hidden;
  }
  .banner--before  { left: 0; }
  .banner--after   { left: 406px; }
  .banner--holiday { left: 822px; }
  .banner__shapes { position: absolute; inset: 0; width: 100%; height: 100%; }

  .brand {
    position: absolute; top: 126px; left: 0; right: 0;
    text-align: center;
    font-family: "Open Sans", sans-serif; font-weight: 600;
    font-size: 42px; line-height: 1; color: var(--white);
    letter-spacing: 0.5px;
  }

  .tagline {
    position: absolute; top: 284px; left: 0; right: 0; text-align: center;
    font-family: "Lilita One", sans-serif; font-size: 29px;
    color: var(--yellow); letter-spacing: 0.3px;
  }

  .service {
    position: absolute; top: 450px; left: 0; right: 0; height: 300px;
    display: flex; align-items: center; justify-content: center;
    text-align: center;
    font-family: "Architects Daughter", cursive; font-size: 66px; font-weight: 400;
    line-height: 1.2; text-transform: uppercase; color: var(--white);
  }
  .banner--after .service { font-size: 58px; line-height: 1.1; top: 440px; }
  .banner--holiday .service { color: var(--pink); font-size: 58px; line-height: 1.1; top: 430px; }

  .web {
    position: absolute; top: 768px; left: 0; right: 0; height: 120px;
    display: flex; align-items: center; justify-content: center; gap: 12px;
    font-family: "Open Sans", sans-serif; font-size: 29px; color: var(--yellow);
  }
  .web__icon { width: 28px; height: 22px; }
</style>
</head>
<body>
<main class="banner-set">

  <section class="banner banner--before">
    <svg class="banner__shapes" viewBox="0 0 472 1110" preserveAspectRatio="none" aria-hidden="true">
      <rect width="472" height="1110" fill="var(--charcoal)"/>
      <polygon points="0,475 172,558 472,492 472,960 0,960" fill="var(--blue)"/>
      <polygon points="140,535 472,388 472,492 172,558" fill="var(--pink)"/>
    </svg>
    <p class="brand">Play Haven</p>
    <p class="tagline">Letting kids be kids</p>
    <h2 class="service">Before<br>School<br>Care</h2>
    <p class="web">
      <svg class="web__icon" viewBox="0 0 28 22" aria-hidden="true"><g fill="none" stroke="currentColor" stroke-width="1.6"><circle cx="18" cy="10" r="7"/><ellipse cx="18" cy="10" rx="3" ry="7"/><line x1="11" y1="10" x2="25" y2="10"/><line x1="13" y1="15" x2="2" y2="21"/></g></svg>
      www.playhaven.co.nz
    </p>
  </section>

  <section class="banner banner--after">
    <svg class="banner__shapes" viewBox="0 0 472 1110" preserveAspectRatio="none" aria-hidden="true">
      <rect width="472" height="1110" fill="var(--charcoal)"/>
      <polygon points="0,475 172,558 472,492 472,960 0,960" fill="var(--pink)"/>
      <polygon points="140,535 472,388 472,492 172,558" fill="var(--blue)"/>
    </svg>
    <p class="brand">Play Haven</p>
    <p class="tagline">Letting kids be kids</p>
    <h2 class="service">After<br>School<br>Care &amp;<br>Activities</h2>
    <p class="web">
      <svg class="web__icon" viewBox="0 0 28 22" aria-hidden="true"><g fill="none" stroke="currentColor" stroke-width="1.6"><circle cx="18" cy="10" r="7"/><ellipse cx="18" cy="10" rx="3" ry="7"/><line x1="11" y1="10" x2="25" y2="10"/><line x1="13" y1="15" x2="2" y2="21"/></g></svg>
      www.playhaven.co.nz
    </p>
  </section>

  <section class="banner banner--holiday">
    <svg class="banner__shapes" viewBox="0 0 472 1110" preserveAspectRatio="none" aria-hidden="true">
      <rect width="472" height="1110" fill="var(--charcoal)"/>
      <polygon points="0,475 172,558 472,492 472,960 0,960" fill="var(--grey)"/>
      <polygon points="140,535 472,388 472,492 172,558" fill="var(--yellow)"/>
    </svg>
    <p class="brand">Play Haven</p>
    <p class="tagline">Letting kids be kids</p>
    <h2 class="service">School<br>Holiday<br>Activities</h2>
    <p class="web">
      <svg class="web__icon" viewBox="0 0 28 22" aria-hidden="true"><g fill="none" stroke="currentColor" stroke-width="1.6"><circle cx="18" cy="10" r="7"/><ellipse cx="18" cy="10" rx="3" ry="7"/><line x1="11" y1="10" x2="25" y2="10"/><line x1="13" y1="15" x2="2" y2="21"/></g></svg>
      www.playhaven.co.nz
    </p>
  </section>

</main>
</body>
</html>
```